Mechanical Engineer Business Card Design (Unemployed)

I am unemployed and actively looking for a job in Canada. I will be using this business card when I meet potential employers or in networking events.I would love to have the engraved writing style (as if it is engraved on the card). Some examples attached.I would love to have a personalized logo that represents my 2 majors. The final design should have a professional look that can stand out if attached to a resume. Jobs I am applying for are in construction, mining, oil and gas, Aerospace, manufacturing and whatever field I can be integrated in.A metallic look on the back is ok. but the front have to be sort of can be written on. you can also try to add my profilelink profile https://ca.profilelink.example/in/tomasvelder
On the front or back, I would love to have the symbol of mail and phone rather than the words. that saves spaceAmaze me guys.

Target Market(s)

Engineering

Industry/Entity Type

Engineering

Contact Information for Business Card

Tomas Velder
Mechanical Engineer

Phone number: +1 (555) 014 - 2738
email: veldertomas@mailbox.example

Requirements
Must have
• PERSONALIZED and brand new Simple Logo
• Professional look
• Engraved writing for the name
• Help stand out when attached on CV
Nice to have
• Metallic back look

```html
<!DOCTYPE html>
<html lang="en">
<head>
<meta charset="utf-8">
<title>Tomas Velder – Business Card</title>
<link rel="stylesheet" href="https://fonts.googleapis.com/css2?family=PT+Sans:wght@400;700&display=swap">
<style>
  :root {
    --backdrop: #6a4531;
    --card-white: #ececec;
    --ink: #1f1f1f;
    --ink-soft: #2e2e2e;
    --mark-light: #d9d9d9;
    --mark-metal: #d2d2d2;
    --metal-dark: #a9a9a9;
    --metal-mid: #c9c9c9;
    --metal-light: #f2f2f2;
    --panel-white: #ffffff;
    --mark-dark: #232323;
  }
  * { box-sizing: border-box; margin: 0; padding: 0; }
  html, body { width: 1200px; height: 847px; overflow: hidden; }
  body {
    background: var(--backdrop);
    font-family: "PT Sans", sans-serif;
    position: relative;
  }
  .card {
    position: absolute;
    width: 564px;
    height: 336px;
    left: 83px;
  }
  .card-front { top: 62px; background: var(--card-white); }
  .card-back {
    top: 451px;
    background: linear-gradient(100deg, var(--metal-dark) 0%, var(--metal-mid) 30%, var(--metal-light) 62%, var(--metal-mid) 85%, var(--metal-dark) 100%);
  }
  .holder-name {
    position: absolute;
    left: 28px;
    top: 82px;
    font-size: 27px;
    font-weight: 700;
    color: var(--ink);
    letter-spacing: 0.2px;
  }
  .holder-title {
    position: absolute;
    left: 28px;
    top: 117px;
    font-size: 14px;
    color: var(--ink-soft);
  }
  .contact-list {
    position: absolute;
    left: 28px;
    top: 188px;
    list-style: none;
  }
  .contact-item {
    display: flex;
    align-items: center;
    gap: 8px;
    font-size: 14px;
    color: var(--ink);
    height: 23.5px;
  }
  .contact-icon { width: 12px; height: 12px; flex: none; }
  .contact-icon.square { background: var(--ink); width: 10px; height: 10px; margin: 0 1px; }
  .brand-name {
    position: absolute;
    font-weight: 700;
    text-align: center;
    white-space: nowrap;
  }
  .card-front .brand-name {
    left: 380px; top: 150px; width: 170px;
    font-size: 24px; color: var(--mark-light);
  }
  .card-back .brand-name {
    left: 190px; top: 150px; width: 184px;
    font-size: 26px; color: var(--mark-metal);
  }
  .logo-panel {
    position: absolute;
    left: 770px;
    top: 248px;
    width: 348px;
    height: 344px;
    background: var(--panel-white);
  }
  .logo-panel-label {
    position: absolute;
    top: 10px;
    width: 100%;
    text-align: center;
    font-size: 20px;
    color: var(--ink);
  }
  .logo-panel .brand-name {
    left: 0; top: 158px; width: 100%;
    font-size: 30px; color: var(--mark-dark);
  }
</style>
</head>
<body>
  <section class="card card-front">
    <h1 class="holder-name">Tomas Velder</h1>
    <p class="holder-title">Mechanical Engineer</p>
    <ul class="contact-list">
      <li class="contact-item"><span class="contact-icon square"></span>tomasvelder</li>
      <li class="contact-item">
        <svg class="contact-icon" viewBox="0 0 12 12"><path d="M1 4 Q6 1 11 4 L10 5.5 L8 5 L8 4 Q6 3.4 4 4 L4 5 L2 5.5 Z M3.5 6 L8.5 6 L10 10.5 L2 10.5 Z" fill="#1f1f1f"/></svg>
        +1 (555) 014 - 2738
      </li>
      <li class="contact-item">
        <svg class="contact-icon" viewBox="0 0 12 12"><rect x="0.5" y="2.5" width="11" height="7.5" fill="#1f1f1f"/><path d="M0.8 2.8 L6 7 L11.2 2.8" fill="none" stroke="#ececec" stroke-width="1"/></svg>
        veldertomas@mailbox.example
      </li>
    </ul>
    <span class="brand-name">Tomas Velder</span>
  </section>

  <section class="card card-back">
    <span class="brand-name">Tomas Velder</span>
  </section>

  <section class="logo-panel">
    <p class="logo-panel-label">LOGO DESIGN</p>
    <span class="brand-name">Tomas Velder</span>
  </section>
</body>
</html>
```